Quorvex business card design

create modern and tech looking business card that is clean but effectively communciates that we are a cloud communications company.
Should have at minimum:
Employee Name
Postion
Phone Number
Email
website
create modern and tech looking business card that is clean but effectively communciates that we are a cloud communications company. We have two logo color schemes (attached) so would like to see designs both ways
Should have at minimum:
Employee Name
Postion
Phone Number
Email
website

```html
<!DOCTYPE html>
<html lang="en">
<head>
<meta charset="utf-8">
<title>Quorvex Business Card</title>
<link href="https://fonts.googleapis.com/css2?family=Roboto:wght@400;500;700&family=Roboto+Condensed:wght@500;700&display=swap" rel="stylesheet">
<style>
  :root {
    --backdrop: #2a2a2a;
    --paper: #f3f3f3;
    --ink: #474747;
    --purple: #612d86;
    --cyan: #29b6d6;
    --white: #ffffff;
  }
  * { margin: 0; padding: 0; box-sizing: border-box; }
  html, body {
    width: 1200px; height: 960px; overflow: hidden;
    background: var(--backdrop);
    font-family: "Roboto", Arial, sans-serif;
  }
  .stage { position: relative; width: 1200px; height: 960px; }

  .card { position: absolute; width: 600px; height: 342px; overflow: hidden; }

  /* Front */
  .card-front { left: 314px; top: 113px; background: var(--paper); }
  .side-band { position: absolute; right: 0; top: 0; width: 36px; height: 100%; background: var(--cyan); }
  .pixel { position: absolute; width: 20px; height: 20px; }
  .pixel-cyan { left: 524px; top: 33px; background: var(--cyan); }
  .pixel-white { left: 563px; top: 37px; background: var(--white); }
  .pixel-purple { left: 499px; top: 80px; background: var(--purple); }

  .brand {
    position: absolute; left: 40px; top: 72px;
    display: flex; align-items: center; gap: 14px;
  }
  .brand-mark { width: 18px; height: 18px; background: var(--purple); }
  .brand-name {
    font-family: "Roboto", Arial, sans-serif; font-weight: 500;
    font-size: 34px; letter-spacing: 2px; color: var(--ink);
  }

  .person { position: absolute; right: 74px; top: 170px; text-align: right; }
  .person-name {
    font-family: "Roboto Condensed", "Arial Narrow", sans-serif;
    font-weight: 700; font-size: 21px; color: var(--purple); line-height: 26px;
  }
  .person-role {
    font-family: "Roboto Condensed", "Arial Narrow", sans-serif;
    font-weight: 500; font-size: 15px; color: var(--cyan); line-height: 22px;
  }

  .contacts { position: absolute; left: 51px; top: 242px; list-style: none; }
  .contacts li {
    display: flex; align-items: center; gap: 8px;
    font-size: 14px; color: var(--ink); line-height: 19px;
  }
  .contacts svg { width: 13px; height: 13px; fill: var(--purple); flex: none; }

  /* Back */
  .card-back { left: 311px; top: 472px; background: var(--purple); }
  .back-brand {
    position: absolute; left: 0; right: 0; top: 140px;
    display: flex; justify-content: center; align-items: center; gap: 16px;
  }
  .back-brand .brand-mark { width: 22px; height: 22px; background: var(--cyan); }
  .back-brand .brand-name { color: var(--white); font-size: 40px; }
  .back-url {
    position: absolute; left: 0; right: 0; top: 283px; text-align: center;
    color: var(--white); font-size: 14px; letter-spacing: 6px;
  }
</style>
</head>
<body>
<main class="stage">
  <section class="card card-front">
    <div class="side-band"></div>
    <div class="pixel pixel-cyan"></div>
    <div class="pixel pixel-white"></div>
    <div class="pixel pixel-purple"></div>

    <div class="brand">
      <span class="brand-mark"></span>
      <span class="brand-name">QUORVEX</span>
    </div>

    <div class="person">
      <p class="person-name">JOHN SMITH</p>
      <p class="person-role">CEO/FOUNDER</p>
    </div>

    <ul class="contacts">
      <li>
        <svg viewBox="0 0 24 24" aria-hidden="true"><path d="M6.6 10.8a15.1 15.1 0 0 0 6.6 6.6l2.2-2.2a1 1 0 0 1 1-.25 11.4 11.4 0 0 0 3.6.57 1 1 0 0 1 1 1V20a1 1 0 0 1-1 1A17 17 0 0 1 3 4a1 1 0 0 1 1-1h3.5a1 1 0 0 1 1 1c0 1.25.2 2.45.57 3.6a1 1 0 0 1-.25 1z"/></svg>
        555 014 2738
      </li>
      <li>
        <svg viewBox="0 0 24 24" aria-hidden="true"><path d="M2 5h20v14H2z M2 5l10 8 10-8" fill="var(--purple)"/><path d="M3.5 6.5l8.5 6.8 8.5-6.8" fill="none" stroke="#f3f3f3" stroke-width="1.6"/></svg>
        name@quorvex.com
      </li>
      <li>
        <svg viewBox="0 0 24 24" aria-hidden="true"><circle cx="12" cy="12" r="10"/><path d="M7 8c2 0 3 1 3 3s-2 2-2 4M14 5c0 2 2 2 3 3s0 3 1 4" fill="none" stroke="#f3f3f3" stroke-width="1.6"/></svg>
        www.quorvex.com
      </li>
    </ul>
  </section>

  <section class="card card-back">
    <div class="back-brand">
      <span class="brand-mark"></span>
      <span class="brand-name">QUORVEX</span>
    </div>
    <p class="back-url">www.quorvex.com</p>
  </section>
</main>
</body>
</html>
```